Solo consultant in research/analytics/data science space needs new business card

I need a new business card to promote my solo business as creative problem solver and consultant. I work on business projects for sales and market research and analytics, customer/market insights, and data science. I provide clients data-informed insights and ideas to enhance their businesses. My initial tagline: 'Make your data work for YOU.'

People should hire me because of my diverse background. Because of my Ph.D. in Political Science I have a strong background in research and analytics, project design and management, and communications skills. With my experience as a marketing analyst, a volunteer on non-profit projects, and currently as research consultant I have worked on projects within various industries. I also have a taste for improvisation so I enjoy thinking creatively and appreciate design thinking.

As an introduction to my background: Clients might want to hire me for many types of projects. Clients might wish to understand who their best customers are and how to characterize them. Maybe clients want to know how their customers feel about a certain product or service. Clients might want to know more about their local market area and overall industry. Clients might want to know whether their marketing programs are effective or else what drives their sales revenue. Perhaps clients want to use their data to create something useful for themselves or their customers.

One client hired me to help them decide whether to expand their services to newer customers. I gathered and analyzed information about the local area – the characteristics of people living there as well as the client’s competitors – and described trends and implications. The client was very pleased with the results and submitted them to superiors for approval to move forward.

For another client – who was looking to purchase a house in a metropolitan area – I gathered population and school data about the area. With this, I created an interactive mapping tool so they could zoom in on neighborhoods and learn more about them before they selected a neighborhood to purchase a house. They were happy with the results of my work.

When I worked as a marketing analyst for a consulting firm, a Vice President of Marketing hired us to discover whether or not the company’s marketing programs (i.e. coupons and discounts) were effective. I analyzed their data and our team discovered their marketing was indeed effective. He was very happy and used this to justify their programs to the Finance department (who thought such programs lost revenue).

- Marcus Delano Whitby, Ph.D.

Target Market(s)

Future clients and employers. The most immediate target markets will be other service providers such as consulting companies, marketing firms and ad agencies. I will also use this for meeting with clients in various industries.

Industry/Entity Type

Consulting

Contact Information for Business Card

Since it is my first real business card as a solo practitioner, I want to make an excellent first impression. I want this useful in case someone hires me to work on projects or else hire me to work within a firm or company. The card should convey competence and some creativity while also being neither stuffy nor a data geek.

Colors

Designer to choose colors to be used in the design.

Requirements
Nice to have
• Attached are the starting efforts at the card to add some color. It will be nice to use my name and descriptors on one side and tagline on the other. If anyone has better ideas, I will love to see them!

```html
<!DOCTYPE html>
<html lang="en">
<head>
<meta charset="utf-8">
<title>Marcus Delano Whitby – Business Card</title>
<link href="https://fonts.googleapis.com/css2?family=Arimo:wght@400&family=Noto+Sans:wght@400;700&display=swap" rel="stylesheet">
<style>
  :root {
    --page: #ffffff;
    --card-dark: #2d2d2d;
    --accent: #e05d4c;
    --cream: #f8f1e3;
    --ink: #141414;
    --white: #ffffff;
  }
  html, body {
    margin: 0;
    width: 1200px;
    height: 1200px;
    overflow: hidden;
    background: var(--page);
  }
  .canvas { position: relative; width: 1200px; height: 1200px; }
  .card {
    position: absolute;
    left: 234px;
    width: 700px;
    height: 405px;
    border-radius: 20px;
    background: var(--card-dark);
    overflow: hidden;
    box-shadow: 10px 14px 16px rgba(0,0,0,0.35);
  }
  .card--front { top: 146px; }
  .card--back { top: 619px; }

  .tagline {
    position: absolute;
    inset: 0;
    display: flex;
    align-items: center;
    justify-content: center;
    margin: 0;
    padding-bottom: 28px;
    text-align: center;
    font-family: "Arimo", Arial, sans-serif;
    font-weight: 400;
    font-size: 64px;
    line-height: 84px;
    color: var(--white);
  }

  .header-band {
    position: absolute;
    left: 0; top: 0;
    width: 100%;
    height: 186px;
    background: var(--accent);
  }
  .name {
    position: absolute;
    left: 50px; top: 68px;
    margin: 0;
    font-family: "Noto Sans", Verdana, sans-serif;
    font-weight: 700;
    font-size: 41px;
    line-height: 50px;
    letter-spacing: 0.5px;
    color: var(--cream);
    white-space: nowrap;
  }
  .disciplines {
    position: absolute;
    left: 51px; top: 122px;
    margin: 0;
    font-family: "Noto Sans", Verdana, sans-serif;
    font-size: 19px;
    line-height: 26px;
    color: var(--ink);
    white-space: nowrap;
  }

  .details {
    position: absolute;
    left: 51px; top: 226px;
    font-family: "Arimo", Arial, sans-serif;
    color: var(--white);
  }
  .role {
    font-family: "Noto Sans", Verdana, sans-serif;
    font-size: 27px;
    line-height: 34px;
    color: var(--accent);
  }
  .location { font-size: 19px; line-height: 30px; }
  .phone { font-size: 21px; line-height: 34px; }

  .divider {
    position: absolute;
    left: 348px; top: 206px;
    width: 4px; height: 160px;
  }

  .contacts {
    position: absolute;
    left: 398px; top: 232px;
    margin: 0; padding: 0;
    list-style: none;
    font-family: "Arimo", Arial, sans-serif;
    font-size: 19px;
    color: var(--white);
  }
  .contacts li {
    display: flex;
    align-items: center;
    height: 33px;
  }
  .contacts .icon {
    width: 22px; height: 22px;
    margin-right: 14px;
    flex: none;
  }
</style>
</head>
<body>
<main class="canvas">
  <section class="card card--front">
    <p class="tagline">Make your data<br>work for YOU.</p>
  </section>

  <section class="card card--back">
    <div class="header-band"></div>
    <h1 class="name">Marcus Delano Whitby, Ph.D.</h1>
    <p class="disciplines">Research/Analytics – Customer Intelligence – Data Science</p>

    <div class="details">
      <div class="role">Consultant</div>
      <div class="location">Lisbon, PT</div>
      <div class="phone">+351 912 604 318</div>
    </div>

    <svg class="divider" viewBox="0 0 4 160" aria-hidden="true">
      <path d="M2 0 L3 80 L2 160 L1 80 Z" fill="var(--cream)"/>
    </svg>

    <ul class="contacts">
      <li>
        <svg class="icon" viewBox="0 0 22 22" aria-hidden="true">
          <rect x="2" y="5" width="18" height="13" fill="none" stroke="#fff" stroke-width="2"/>
          <path d="M2 5 L11 12 L20 5 M2 18 L8.5 10.5 M20 18 L13.5 10.5" fill="none" stroke="#fff" stroke-width="1.6"/>
        </svg>
        <span>mdwhitby70@mailnest.com</span>
      </li>
      <li>
        <svg class="icon" viewBox="0 0 22 22" aria-hidden="true">
          <circle cx="11" cy="11" r="9" fill="#fff"/>
        </svg>
        <span>@MarcusWhitby70</span>
      </li>
      <li>
        <svg class="icon" viewBox="0 0 22 22" aria-hidden="true">
          <circle cx="11" cy="11" r="9" fill="none" stroke="#fff" stroke-width="2"/>
          <ellipse cx="11" cy="11" rx="4" ry="9" fill="none" stroke="#fff" stroke-width="1.5"/>
          <path d="M2 11 H20" stroke="#fff" stroke-width="1.5"/>
        </svg>
        <span>Marcusdelanowhitby.com</span>
      </li>
    </ul>
  </section>
</main>
</body>
</html>
```